Webdesign für Arbeitsschutz
Zielgruppe
Grundlage für ein funktionierendes Beschäftigungssystem ist die Schaffung und der Erhalt sicherer und menschengerechter Arbeitsbedingungen. Ein effizienter Arbeitsschutz und eine wirksame Unfallvermeidung sind hierfür besonders wichtig, vor allem auch im Hinblick auf die Herausforderungen einer durch digitalen Wandel immer schnelleren und anspruchsvolleren Arbeitswelt. Sicherheit und Gesundheit bei der Arbeit sind deshalb wichtige Arbeitsschwerpunkte im Landesamt für Betriebe und Sozialwesen. Ziel ist es, die Beschäftigten wirksam vor Gefahren und gesundheitlichen Schädigungen zu schützen. Verlässliche gesetzliche Grundlagen und rechtssichere Rahmenbedingungen für alle Unternehmen sind dafür unerlässlich.
Das wichtigste Grundlagengesetz für den betrieblichen Arbeitsschutz ist das Arbeitsschutzgesetz (ArbSchG). Es verpflichtet den Arbeitgeber, Gesundheitsgefährdungen am Arbeitsplatz zu beurteilen und über notwendige Schutzmaßnahmen zu entscheiden. Der Arbeitgeber hat für eine funktionierende Arbeitsschutzorganisation im Betrieb zu sorgen. Dies kann besonders wirksam durch eine nachhaltige Einbindung des Arbeits- und Gesundheitsschutzes in die Strukturen und Abläufe eines Unternehmens erreicht werden.
Aufgabenstellung
Gerne eine helle Seite mit schöner integration des Logo´s in die Homepage
Ich möchte keine exakte Kopie der Internet-Seite haben, aber alle Inhalte die Lemm-Arbeitsschutz anbietet (inkl. Rückrufservice, Anbringen von Referenz-Logos, Navigationsmenü)
Die Gestaltung der Hauptseite mit Farbe sollte bitte mit den vorhandenen Logo harmonieren. Die Aufteilung wo sich die Bausteine (Rückrufservice etc.) befindet sollte übersichtlich angebracht sein.

```html
<!DOCTYPE html>
<html lang="de">
<head>
<meta charset="utf-8">
<title>Arbeitsschutz &amp; Gesundheitsdienst Alpenland GmbH</title>
<link href="https://fonts.googleapis.com/css2?family=Poppins:wght@300;400;500;600;700&display=swap" rel="stylesheet">
<style>
:root{
  --teal:#2f6b80;
  --teal-dark:#285d70;
  --teal-soft:#6f9fb2;
  --ink:#2b2b2b;
  --muted:#666;
  --paper:#ffffff;
  --mist:#f7f7f7;
}
*{box-sizing:border-box;margin:0;padding:0}
html,body{width:1200px;height:3324px;overflow:hidden}
body{position:relative;font-family:'Poppins',sans-serif;color:var(--ink);background:var(--paper)}
.abs{position:absolute}
a{color:inherit;text-decoration:none}

/* header */
.site-header{position:absolute;top:0;left:0;width:1200px;height:112px;background:var(--paper)}
.brand{position:absolute;left:62px;top:40px;display:flex;align-items:center;gap:10px;color:var(--teal);font-size:10px;line-height:13px;font-weight:400}
.brand-mark{width:12px;height:12px;background:var(--teal)}
.main-nav{position:absolute;left:415px;top:38px;display:flex;height:74px}
.main-nav a{font-size:10.5px;font-weight:500;color:var(--teal);padding:12px 8px 0;height:74px}
.main-nav a.active{background:var(--teal);color:#fff;padding:12px 13px 0}
.head-icon{position:absolute;top:41px;width:31px;height:31px;background:var(--teal);display:flex;align-items:center;justify-content:center}

/* hero */
.hero{position:absolute;top:112px;left:0;width:1200px;height:531px;overflow:hidden}
.hero-photo{position:absolute;inset:0;background:linear-gradient(100deg,#9fc0d8 0%,#dfe8ef 40%,#c9d2df 60%,#5a6a8a 100%)}
.hero-overlay{position:absolute;inset:0}
.hero-title{position:absolute;left:62px;top:172px;color:#fff;font-size:39px;line-height:46px;font-weight:300}
.hero-title strong{font-weight:600;display:block}
.btn-outline{position:absolute;border:2px solid #fff;color:#fff;font-size:13px;display:flex;align-items:center;justify-content:center}

/* section heads */
.sec-head{position:absolute;left:0;width:1200px;display:flex;justify-content:center;align-items:flex-end;gap:10px}
.sec-head h2{font-size:18px;font-weight:500;letter-spacing:.3px}
.sec-head .slash{font-size:30px;color:var(--teal);font-weight:300;line-height:28px}
.sec-head span.sub{font-size:12.5px;color:var(--muted);margin-bottom:-6px}

/* services */
.service{position:absolute;width:250px}
.service h3{font-size:14px;font-weight:500;margin-bottom:12px}
.service p{font-size:11px;line-height:17px;color:var(--muted)}
.service a{display:block;margin-top:8px;font-size:10.5px;font-weight:600;color:var(--teal)}
.service.left{text-align:right}
.svc-icon{position:absolute}
.avatar{position:absolute;left:525px;top:922px;width:150px;height:150px;border-radius:50%;background:linear-gradient(180deg,#2f6b80 0%,#2f6b80 60%,#e6eef3 60%)}
.avatar-caption{position:absolute;left:500px;top:1093px;width:200px;text-align:center;font-size:11px;line-height:19px;font-weight:600;color:var(--teal)}

/* about */
.about{position:absolute;top:1336px;left:0;width:1200px;height:712px;background:var(--mist)}
.about-lead{position:absolute;top:140px;left:0;width:1200px;text-align:center;font-size:13px;line-height:21px;color:var(--teal)}
.card{position:absolute;width:300px;background:var(--teal);color:#fff;text-align:center;padding:32px 30px 0}
.card p{font-size:10.5px;line-height:18px}
.card .btn-outline{position:relative;margin:14px auto 0;width:126px;height:30px;font-size:11.5px;font-weight:600}
.card-title{position:absolute;width:300px;text-align:center;font-size:19px;line-height:22px;font-weight:600;color:var(--ink)}
.connector{position:absolute;height:3px;background:var(--teal)}

/* callback */
.callback{position:absolute;top:2048px;left:0;width:1200px;height:562px;background:linear-gradient(100deg,#5a8ea3 0%,#6f9fb2 50%,#8fb5c4 100%);overflow:hidden}
.callback h2{position:absolute;left:480px;top:84px;font-size:27px;font-weight:600;color:#fff}
.field{position:absolute;border-bottom:1px solid rgba(255,255,255,.8);color:#fff;font-size:12.5px;padding-bottom:12px;display:flex;justify-content:space-between;align-items:center}
.field.small{font-size:10.5px}
.btn-send{position:absolute;left:670px;top:426px;width:156px;height:37px;background:#fff;color:var(--teal);font-size:15px;font-weight:600;display:flex;align-items:center;justify-content:center}

/* references */
.refs{position:absolute;top:2772px;left:340px;width:520px;display:flex;justify-content:space-between;align-items:center}
.refs span{font-size:20px;font-weight:700;color:var(--ink)}

/* footer */
.site-footer{position:absolute;top:2909px;left:0;width:1200px;height:376px;background:var(--mist)}
.foot-title{position:absolute;color:var(--teal);font-size:19px;line-height:32px;font-weight:600}
.contact-list{position:absolute;left:64px;top:144px;list-style:none;font-size:12.5px;color:var(--muted)}
.contact-list li{height:25px;display:flex;align-items:center;gap:12px}
.address{position:absolute;left:64px;top:262px;font-size:12.5px;line-height:25px;color:var(--muted)}
.address strong{color:var(--ink);font-weight:600;font-size:11.5px}
.foot-links{position:absolute;list-style:none;font-size:12.5px;color:var(--muted)}
.foot-links li{height:25px;display:flex;align-items:center;gap:12px}
.foot-links li::before{content:"";width:10px;height:10px;background:var(--ink)}
.foot-brand{position:absolute;left:400px;top:230px;width:400px;text-align:center;color:var(--teal);font-size:18px;line-height:22px;font-weight:400}
.copyright{position:absolute;top:3285px;left:0;width:1200px;height:39px;background:var(--teal);color:#fff;font-size:12px;display:flex;align-items:center;justify-content:center;gap:4px}
.copyright b{font-weight:600}
</style>
</head>
<body>

<header class="site-header">
  <div class="brand"><span class="brand-mark"></span><span>Arbeitsschutz &amp; Gesundheitsdienst<br>Alpenland GmbH</span></div>
  <nav class="main-nav">
    <a class="active" href="#">Startseite</a>
    <a href="#">Beratung &amp; Betreuung</a>
    <a href="#">Seminare</a>
    <a href="#">E-Learning</a>
    <a href="#">Beauftragtenwesen</a>
    <a href="#">Das Unternehmen</a>
    <a href="#">Kontakt</a>
  </nav>
  <div class="head-icon" style="left:1068px"><svg width="13" height="10" viewBox="0 0 13 10"><rect x="0" y="0" width="13" height="10" fill="#fff"/><path d="M0 0 L6.5 5.5 L13 0" stroke="#2f6b80" stroke-width="1.3" fill="none"/></svg></div>
  <div class="head-icon" style="left:1106px"><svg width="13" height="13" viewBox="0 0 24 24"><path fill="#fff" d="M6.6 10.8a15.1 15.1 0 006.6 6.6l2.2-2.2a1 1 0 011-.25 11.4 11.4 0 003.6.6 1 1 0 011 1V20a1 1 0 01-1 1A17 17 0 013 4a1 1 0 011-1h3.5a1 1 0 011 1c0 1.250.2 2.45.6 3.6a1 1 0 01-.25 1z"/></svg></div>
</header>

<section class="hero">
  <div class="hero-photo" role="img" aria-label="Foto: Mann im karierten Hemd hält einen orangefarbenen Schutzhelm, im Hintergrund ein Kran mit Last"></div>
  <svg class="hero-overlay" width="1200" height="531"><polygon points="0,0 587,0 329,531 0,531" fill="#2f6b80" fill-opacity=".82"/></svg>
  <h1 class="hero-title">Mit Sicherheit Mehr<strong>Sicherheit</strong></h1>
  <a class="btn-outline" style="left:62px;top:312px;width:156px;height:36px" href="#">Mehr anzeigen</a>
</section>

<div class="sec-head" style="top:700px"><h2>DIENSTLEISTUNGEN</h2><span class="slash">/</span><span class="sub">Sie wissen, was wir anbieten</span></div>

<div class="service left" style="left:119px;top:818px"><h3>Wir stellen ein</h3><p>Informieren Sie sich über<br>unsere Stellenangebote.</p><a href="#">zu den Stellenausschreibungen</a></div>
<svg class="svc-icon" style="left:390px;top:815px" width="54" height="46" viewBox="0 0 54 46" fill="none" stroke="#2f6b80" stroke-width="3"><circle cx="20" cy="13" r="10"/><path d="M2 44c0-11 8-18 18-18s18 7 18 18z"/><path d="M44 12v14M37 19h14"/></svg>

<div class="service left" style="left:119px;top:989px"><h3>Arbeitsschutz</h3><p>Sicherheit geht vor! Wir betreuen Ihr<br>Unternehmen als externe Fachkraft für<br>Arbeitssicherheit.</p><a href="#">mehr zum Arbeitsschutz</a></div>
<svg class="svc-icon" style="left:390px;top:992px" width="38" height="46" viewBox="0 0 38 46" fill="none" stroke="#2f6b80" stroke-width="3"><path d="M19 2L3 8v14c0 11 7 18 16 22 9-4 16-11 16-22V8z"/><path d="M11 23l6 6 11-12"/></svg>

<div class="service left" style="left:119px;top:1167px"><h3>Seminare</h3><p>Wir bieten eine Vielzahl von fachspe-<br>zifischen Seminaren rund um den<br>Arbeitsschutz.</p><a href="#">Übersicht unserer Seminare</a></div>
<svg class="svc-icon" style="left:390px;top:1160px" width="54" height="48" viewBox="0 0 54 48" fill="none" stroke="#2f6b80" stroke-width="2.5"><circle cx="9" cy="6" r="4.5" fill="#2f6b80"/><path d="M9 12v18M9 30l-4 16M9 30l4 16M9 16l12 -4"/><rect x="20" y="6" width="32" height="22"/><path d="M36 28v8M30 46l6-10 6 10"/></svg>

<svg class="svc-icon" style="left:755px;top:815px" width="56" height="40" viewBox="0 0 56 40" fill="none" stroke="#2f6b80" stroke-width="3"><rect x="7" y="2" width="42" height="28" rx="2"/><path d="M1 35h54"/></svg>
<div class="service" style="left:832px;top:818px"><h3>E-Learning</h3><p>Sicherheitsunterweisungen online<br>mit E-Learning - flexibel,unkompliziert<br>und zeitsparend.</p><a href="#">alles zum Thema E-Learning</a></div>

<svg class="svc-icon" style="left:780px;top:988px" width="34" height="50" viewBox="0 0 34 50" fill="none" stroke="#2f6b80" stroke-width="3"><path d="M10 26V6a3 3 0 016 0v16M16 20V3a3 3 0 016 0v19M22 20V6a3 3 0 016 0v20M28 24v-8a3 3 0 016 0v14c0 10-6 18-15 18-6 0-9-3-13-9L2 30a3 3 0 015-3l3 4"/></svg>
<div class="service" style="left:832px;top:989px"><h3>Beauftragtenwesen</h3><p>Übernahme der Beauftragten Funkt-<br>ionen - von Gefahrstoffen bis hin<br>zum Brandschutz.</p><a href="#">mehr zum Beauftragtenwesen</a></div>

<svg class="svc-icon" style="left:757px;top:1165px" width="56" height="46" viewBox="0 0 56 46" fill="none" stroke="#2f6b80" stroke-width="3"><rect x="12" y="2" width="42" height="32" rx="2"/><path d="M12 10h42"/><path d="M2 30h14l6 6H2z" fill="#2f6b80"/><path d="M2 38h20v6H2z" fill="#2f6b80"/></svg>
<div class="service" style="left:832px;top:1167px;width:300px"><h3>StoffPlan - Gefahrstoff Softwarelösung</h3><p>Gefahrstoff-Management, einfach  wie<br>nie zuvor! Flexibel und anpas-sbar<br>an Ihre Prozesse.</p><a href="#">mehr zu StoffPlan</a></div>

<div class="avatar" role="img" aria-label="Illustration: Sicherheitsfachkraft in Uniform mit Mütze"></div>
<p class="avatar-caption">Ihr Ingenieur- und Sachver-<br>ständigenbüro für Arbeitssi-<br>cherheit</p>

<section class="about">
  <div class="sec-head" style="top:84px"><h2>ÜBER UNS</h2><span class="slash">/</span><span class="sub">unsere Arbeit</span></div>
  <p class="about-lead">Ihr Ingenieur- und Sachverständigenbüro für<br>Arbeitssicherheit</p>

  <svg class="abs" style="left:182px;top:288px" width="62" height="46" viewBox="0 0 62 46"><path d="M4 40c0-20 12-36 30-36 14 0 24 10 24 24v6H20c-6 0-10 3-16 6z" fill="#2f6b80"/><path d="M20 34c0-14 6-24 16-28" stroke="#f7f7f7" stroke-width="3" fill="none"/></svg>
  <p class="card-title" style="left:62px;top:354px">Lemm<br>Arbeitsschutz</p>

  <svg class="abs" style="left:576px;top:222px" width="48" height="58" viewBox="0 0 48 58" fill="none" stroke="#2f6b80" stroke-width="5"><path d="M24 3L4 10v17c0 14 9 23 20 28 11-5 20-14 20-28V10z"/><path d="M14 29l8 8 13-15"/></svg>
  <p class="card-title" style="left:450px;top:292px">Ihre Sicherheit Ist Unsere<br>Aufgabe!</p>

  <svg class="abs" style="left:964px;top:286px" width="46" height="46" viewBox="0 0 46 46"><circle cx="18" cy="11" r="9" fill="#2f6b80"/><path d="M2 44c0-14 7-22 16-22 6 0 10 3 13 7v15z" fill="#2f6b80"/><path d="M34 24l-9 4v7c0 6 4 9 9 11 5-2 9-5 9-11v-7z" fill="#2f6b80" stroke="#f7f7f7" stroke-width="2"/></svg>
  <p class="card-title" style="left:837px;top:354px">Fachkraft für<br>Arbeitssicherheit</p>

  <div class="connector" style="left:362px;top:486px;width:88px"></div>
  <div class="connector" style="left:750px;top:486px;width:87px"></div>

  <div class="card" style="left:62px;top:420px;height:200px"><p>Lemm Arbeitsschutz ist Ihr zertifizierter Dienstleister für den Raum Karlsruhe und die Region Rhein-Neckar, wenn es um die betriebliche Sicherheit geht.Wir bieten unseren Kunden als externe</p><a class="btn-outline" href="#">Lesen Sie mehr</a></div>
  <div class="card" style="left:450px;top:356px;height:200px"><p>Die Implementierung des Arbeits- und Gesundheitsschutzes ist für alle Betriebe egal in welcher Größe und Branche ein wichtiges Thema, denn der Gesetzgeber verpflichtet Unternehmen zur Umsetzung der</p><a class="btn-outline" href="#">Lesen Sie mehr</a></div>
  <div class="card" style="left:837px;top:420px;height:200px"><p>Wir unterstützen Sie als Fachkraft für Arbeitssicherheit bei der Erstellung der Gefährdungsbeurteilung, den regelmäßigen Betriebsbegehungen sowie bei den jährlichen Sicherheitsunterweisungen</p><a class="btn-outline" href="#">Lesen Sie mehr</a></div>
</section>

<section class="callback" role="img" aria-label="Foto: Team im Callcenter mit Headsets, bläulich eingefärbt">
  <h2>Unser Rückrufservice</h2>
  <div class="field" style="left:480px;top:190px;width:161px">Anrede*<svg width="11" height="7"><path d="M1 1l4.5 4.5L10 1" stroke="#fff" stroke-width="1.6" fill="none"/></svg></div>
  <div class="field" style="left:671px;top:190px;width:156px">Name *</div>
  <div class="field" style="left:862px;top:190px;width:157px">Vorname *</div>
  <div class="field" style="left:480px;top:250px;width:275px">Firma *</div>
  <div class="field" style="left:792px;top:250px;width:227px">Telefonr. *</div>
  <div class="field" style="left:480px;top:304px;width:539px">Betreff *</div>
  <div class="field small" style="left:480px;top:366px;width:156px">Wochentag:<svg width="11" height="7"><path d="M1 1l4.5 4.5L10 1" stroke="#fff" stroke-width="1.6" fill="none"/></svg></div>
  <div class="field small" style="left:674px;top:366px;width:156px">Wochentag:<svg width="11" height="7"><path d="M1 1l4.5 4.5L10 1" stroke="#fff" stroke-width="1.6" fill="none"/></svg></div>
  <div class="field small" style="left:862px;top:366px;width:157px">Wochentag:<svg width="11" height="7"><path d="M1 1l4.5 4.5L10 1" stroke="#fff" stroke-width="1.6" fill="none"/></svg></div>
  <a class="btn-send" href="#">absenden</a>
</section>

<div class="sec-head" style="top:2690px"><h2>AUSZUG AUS UNSEREN REFERENZEN</h2><span class="slash">/</span><span class="sub">die besten Dienstleistungen</span></div>
<div class="refs"><span>Solvita</span><span>Hemsner</span><span>Kalbo</span><span>Transtal</span></div>

<footer class="site-footer">
  <p class="foot-title" style="left:64px;top:64px">Zögern Sie nicht, kontaktieren<br>Sie uns.</p>
  <ul class="contact-list">
    <li><svg width="12" height="12" viewBox="0 0 24 24"><path fill="#2b2b2b" d="M6.6 10.8a15.1 15.1 0 006.6 6.6l2.2-2.2a1 1 0 011-.25 11.4 11.4 0 003.6.6 1 1 0 011 1V20a1 1 0 01-1 1A17 17 0 013 4a1 1 0 011-1h3.5a1 1 0 011 1c0 1.25.2 2.45.6 3.6a1 1 0 01-.25 1z"/></svg>+49 6221 58120 - 0</li>
    <li><svg width="12" height="12" viewBox="0 0 24 24"><path fill="#2b2b2b" d="M6.6 10.8a15.1 15.1 0 006.6 6.6l2.2-2.2a1 1 0 011-.25 11.4 11.4 0 003.6.6 1 1 0 011 1V20a1 1 0 01-1 1A17 17 0 013 4a1 1 0 011-1h3.5a1 1 0 011 1c0 1.25.2 2.45.6 3.6a1 1 0 01-.25 1z"/></svg>+49 6221 58120 - 19</li>
    <li><svg width="12" height="9"><rect width="12" height="9" fill="#2b2b2b"/><path d="M0 0l6 5 6-5" stroke="#f7f7f7" stroke-width="1.2" fill="none"/></svg>info(at)lemm-arbeitsschutz.de</li>
    <li><svg width="12" height="12"><circle cx="6" cy="6" r="5" stroke="#2b2b2b" stroke-width="1.4" fill="none"/><path d="M1 6h10M6 1c-3 3-3 7 0 10M6 1c3 3 3 7 0 10" stroke="#2b2b2b" stroke-width="1" fill="none"/></svg>www.lemm-arbeitsschutz.de</li>
  </ul>
  <svg class="abs" style="left:64px;top:272px" width="10" height="14" viewBox="0 0 10 14"><path d="M5 0a5 5 0 015 5c0 4-5 9-5 9S0 9 0 5a5 5 0 015-5z" fill="#2b2b2b"/><circle cx="5" cy="5" r="2" fill="#f7f7f7"/></svg>
  <p class="address" style="left:84px"><strong>LEMM ARBEITSSCHUTZ GMBH &amp; CO. KG</strong><br>Lindenweg 14<br>69190 Walldorf</p>

  <p class="foot-brand">Arbeitsschutz &amp; Gesundheitsdienst<br>Alpenland GmbH</p>

  <p class="foot-title" style="left:932px;top:64px">Software</p>
  <ul class="foot-links" style="left:932px;top:118px"><li>E-Learning</li><li>Gefahrstoff-Software StoffPlan</li></ul>
  <p class="foot-title" style="left:938px;top:196px">Software</p>
  <ul class="foot-links" style="left:938px;top:246px"><li>Impressum</li><li>Datenschutz</li><li>Netzwerk</li><li>Jobs</li></ul>
</footer>

<div class="copyright"><b>Copyright 2015</b> www.lemm-arbeitsschutz.de</div>

</body>
</html>
```